2 x storefront vinyl request

We are transitioning to a storefront office and need two vinyls for the windows.

First vinyl: Use the Dalton Rivers logo, website (www.daltonriversholdings.example) and leasing office number ((555) 318-4472)

Second vinyl: Maintenance Division & phone number (555) 318-4472

```html
<!DOCTYPE html>
<html lang="en">
<head>
<meta charset="utf-8">
<title>Dalton Rivers – Storefront Vinyls</title>
<link href="https://fonts.googleapis.com/css2?family=Open+Sans:wght@400;700;800&family=PT+Serif:wght@700&display=swap" rel="stylesheet">
<style>
  :root {
    --ink: #151515;
    --grey: #a3a3a3;
    --paper: #ffffff;
    --green: #7bc143;
    --backdrop: #ffffff;
  }
  html, body { margin: 0; padding: 0; overflow: hidden; background: var(--backdrop); }
  .canvas { position: relative; width: 1200px; height: 954px; overflow: hidden; background: var(--backdrop); }

  .vinyl {
    position: absolute;
    background: var(--paper);
    box-shadow: 0 0 22px rgba(0,0,0,.45);
    overflow: hidden;
  }
  .vinyl--office { left: 70px; top: 86px; width: 1059px; height: 343px; }
  .vinyl--maintenance { left: 84px; top: 527px; width: 1036px; height: 336px; }

  .wave { position: absolute; left: 0; top: 0; width: 100%; height: 100%; }
  .wave .band { fill: var(--ink); }
  .wave .stripe { fill: var(--grey); }

  .brand-name {
    position: absolute; left: 30px; top: 182px;
    margin: 0;
    font: 700 38px/1.02 "Open Sans", sans-serif;
    color: var(--ink);
    letter-spacing: -0.5px;
  }

  .web-label {
    position: absolute; left: 336px; width: 702px; top: 108px;
    margin: 0; text-align: center;
    font: 400 34px/1 "Open Sans", sans-serif;
    letter-spacing: 5px; color: var(--ink);
  }
  .web-address {
    position: absolute; left: 336px; width: 702px; top: 154px;
    margin: 0; text-align: center;
    font: 700 38px/1 "Open Sans", sans-serif;
    letter-spacing: -0.3px; color: var(--ink);
  }

  .phone { position: absolute; display: flex; align-items: center; }
  .phone-icon { fill: var(--green); flex: none; }
  .phone-number {
    display: inline-block;
    font: 700 104px/1 "PT Serif", serif;
    color: var(--green);
    white-space: nowrap;
    transform: scaleX(0.74);
    transform-origin: left center;
  }
  .vinyl--office .phone { left: 350px; top: 212px; }
  .vinyl--office .phone-icon { width: 92px; height: 112px; margin-right: 12px; }
  .vinyl--maintenance .phone { left: 168px; top: 204px; }
  .vinyl--maintenance .phone-icon { width: 94px; height: 116px; margin-right: 12px; }

  .division-title {
    position: absolute; left: 0; width: 100%; top: 32px;
    margin: 0; text-align: center;
    font: 800 74px/1 "Open Sans", sans-serif;
    color: var(--ink); letter-spacing: -0.5px;
  }
</style>
</head>
<body>
<main class="canvas">

  <section class="vinyl vinyl--office" aria-label="Leasing office window vinyl">
    <svg class="wave" viewBox="0 0 1765 572" preserveAspectRatio="none" aria-hidden="true">
      <path class="stripe" d="M0 100 C260 40 560 30 820 85 C1150 160 1470 190 1765 127 V0 H0 Z"/>
      <path class="band" d="M0 70 C260 30 560 25 820 60 C1150 110 1470 150 1765 85 V0 H0 Z"/>
    </svg>

    <p class="brand-name">DALTON<br>RIVERS<br>PROPERTIES</p>

    <p class="web-label">VISIT OUR WEBSITE:</p>
    <p class="web-address">DALTONRIVERSHOLDINGS.EXAMPLE</p>

    <div class="phone">
      <svg class="phone-icon" viewBox="0 0 80 100" aria-hidden="true">
        <path d="M4 20 C2 12 8 4 16 1 L22 0 L38 26 L30 34 C28 36 28 40 30 44 L48 70 C50 73 54 74 57 72 L65 66 L80 90 L74 96 C66 102 54 101 46 92 C28 72 10 46 4 20 Z"/>
      </svg>
      <span class="phone-number">(555) 318-4472</span>
    </div>
  </section>

  <section class="vinyl vinyl--maintenance" aria-label="Maintenance division window vinyl">
    <svg class="wave" viewBox="0 0 1727 559" preserveAspectRatio="none" aria-hidden="true">
      <path class="stripe" d="M0 361 C280 280 560 238 860 238 C1160 238 1450 300 1727 384 V559 H0 Z"/>
      <path class="band" d="M0 379 C280 305 560 274 860 274 C1160 274 1450 320 1727 403 V559 H0 Z"/>
    </svg>

    <h1 class="division-title">MAINTENANCE DIVISION</h1>

    <div class="phone">
      <svg class="phone-icon" viewBox="0 0 80 100" aria-hidden="true">
        <path d="M4 20 C2 12 8 4 16 1 L22 0 L38 26 L30 34 C28 36 28 40 30 44 L48 70 C50 73 54 74 57 72 L65 66 L80 90 L74 96 C66 102 54 101 46 92 C28 72 10 46 4 20 Z"/>
      </svg>
      <span class="phone-number">(555) 318-4472</span>
    </div>
  </section>

</main>
</body>
</html>
```